Online video and marketing company business cards

Need to get some new business cards designed to fit with our new logo. The cards should be professional, clean and simple.

Cards should have:

Name
Position
2 line address
telephone
mobile
email address
web address

We need to have our logo and if possible say what we do...
ONLINE FILM PRODUCTION & STRATEGY

Marketing

```html
<!DOCTYPE html>
<html lang="en">
<head>
<meta charset="utf-8">
<title>lumenframe – business cards</title>
<link href="https://fonts.googleapis.com/css2?family=Arimo:wght@400;700&display=swap" rel="stylesheet">
<style>
  :root {
    --bg: #e9e6e1;
    --card-white: #ffffff;
    --navy: #1d4a73;
    --navy-deep: #0d3c63;
    --navy-light: #1a5684;
    --sky: #7fb0cf;
    --mist: #dde2e8;
    --grey-text: #6d7076;
    --dark-text: #2b2e33;
  }
  * { margin: 0; padding: 0; box-sizing: border-box; }
  html, body { width: 1200px; height: 1023px; overflow: hidden; }
  body {
    background: var(--bg);
    font-family: "Arimo", Arial, sans-serif;
    position: relative;
  }
  .card {
    position: absolute;
    width: 500px;
    height: 286px;
    overflow: hidden;
    box-shadow: 0 8px 24px rgba(0,0,0,0.18);
  }
  /* Front */
  .card-front { left: 90px; top: 210px; background: var(--card-white); }
  .front-decor {
    position: absolute; left: -90px; top: 120px;
    width: 300px; height: 300px; border-radius: 50%;
    border: 34px solid var(--mist);
  }
  .accent-bar {
    position: absolute; right: 0; top: 44px;
    width: 92px; height: 14px; background: var(--sky);
  }
  .brand { position: absolute; left: 40px; top: 34px; }
  .brand-name {
    display: flex; align-items: center; gap: 8px;
    font-weight: 700; font-size: 34px; color: var(--navy);
    letter-spacing: -0.5px; line-height: 1;
  }
  .brand-dot { width: 22px; height: 22px; border-radius: 50%; background: var(--navy); }
  .tagline {
    margin-top: 8px; margin-left: 30px;
    font-size: 10px; letter-spacing: 0.6px; color: var(--dark-text);
  }
  .contact {
    position: absolute; left: 280px; top: 104px;
    list-style: none; font-size: 13px; color: var(--grey-text);
  }
  .contact li { display: flex; align-items: flex-start; gap: 9px; margin-bottom: 6px; }
  .contact .address { color: var(--dark-text); font-size: 15px; line-height: 1.3; margin-bottom: 10px; }
  .contact svg { flex: none; margin-top: 3px; }
  .person { position: absolute; left: 180px; top: 212px; }
  .person-name { font-weight: 700; font-size: 21px; color: var(--navy); }
  .person-role { font-size: 16px; color: var(--sky); margin-top: 2px; }
  /* Back */
  .card-back {
    left: 620px; top: 520px;
    background: linear-gradient(160deg, var(--navy-light), var(--navy-deep));
  }
  .back-decor {
    position: absolute; left: 120px; top: -60px;
    width: 360px; height: 360px; border-radius: 50%;
    border: 40px solid rgba(255,255,255,0.05);
  }
  .back-brand {
    position: absolute; left: 70px; top: 112px;
    display: flex; align-items: center; gap: 12px;
    font-weight: 700; font-size: 52px; color: #ffffff; line-height: 1;
  }
  .back-brand .brand-dot { width: 30px; height: 30px; background: #ffffff; }
  .web {
    position: absolute; right: 22px; bottom: 20px;
    font-size: 12px; color: rgba(255,255,255,0.85); letter-spacing: 0.3px;
  }
</style>
</head>
<body>
  <section class="card card-front">
    <div class="front-decor" aria-hidden="true"></div>
    <div class="accent-bar"></div>
    <div class="brand">
      <div class="brand-name"><span class="brand-dot"></span>lumenframe</div>
      <p class="tagline">ONLINE FILM PRODUCTION &amp; STRATEGY</p>
    </div>
    <ul class="contact">
      <li class="address">
        <svg width="9" height="12" viewBox="0 0 9 12"><path d="M4.5 0a4.5 4.5 0 0 1 4.5 4.5C9 8 4.5 12 4.5 12S0 8 0 4.5A4.5 4.5 0 0 1 4.5 0z" fill="#1d4a73"/><circle cx="4.5" cy="4.5" r="1.6" fill="#fff"/></svg>
        <span>123 Your location<br>456 Ex7</span>
      </li>
      <li>
        <svg width="10" height="10" viewBox="0 0 10 10"><path d="M2 0l2 2.5-1.2 1.3a6 6 0 0 0 3.4 3.4L7.5 6 10 8l-1.5 2C4 10 0 6 0 1.5z" fill="#1d4a73"/></svg>
        <span>12345 678 999</span>
      </li>
      <li>
        <svg width="8" height="11" viewBox="0 0 8 11"><rect x="0.7" y="0.7" width="6.6" height="9.6" rx="1" fill="none" stroke="#1d4a73" stroke-width="1.4"/></svg>
        <span>123 4567 8990</span>
      </li>
      <li>
        <svg width="11" height="9" viewBox="0 0 11 9"><rect width="11" height="9" fill="#1d4a73"/><path d="M0 0l5.5 4.5L11 0" fill="none" stroke="#fff" stroke-width="1"/></svg>
        <span>info@lumenframe.com</span>
      </li>
    </ul>
    <div class="person">
      <p class="person-name">Your Name</p>
      <p class="person-role">Director</p>
    </div>
  </section>

  <section class="card card-back">
    <div class="back-decor" aria-hidden="true"></div>
    <div class="back-brand"><span class="brand-dot"></span>lumenframe</div>
    <p class="web">www.lumenframe.com</p>
  </section>
</body>
</html>
```